Postcard Design

We are a commercial real estate office located in Mount Kisco. We are holding a rather large event on August 6th for our tenants and in each give a way bag we would like to put a post card. This post card will feature 4 of our buildings on it. We would also like it to say something along the lines of Looking for Office, Medical, Warehouse or Retail space or know someone who is?? Fill out this post card with either your information or the information of a referral & send it back to receive a $25 Gift Card to Velvet Lanes, NY. The point of the post card is to get all guests to refer a friend who is looking for a space. We do need space for an address but we also do need a space on the back that has room for them to fill out all necessary information such as - Name - Email- Referral Name- Phone Number -
Also on the card we would like it to say for all space availabilities visit www.harborlinerealty.example along with some of our contact information. The building information is as follows - the picture with the flowers is 48 Quillfern Ave, N. White Plains, the building with the grass round about in front of it is 212 W Tamsworth Ln. Mount Kisco, the picture that has the close up of the building that is more of a square building is 417/419 W Tamsworth Ln, Mount Kisco and the building with the clouds that is set far back is 586 East Tamsworth Ln, Mount Kisco

NOTE I need all four buildings on the post card. Not just 1. Please list the building addresses by each picture

The name of our company is Harborline Realty - our phone number is 914 608 3157 and the contact for all inquiries is Owen Trezelle

Target Market(s)

Brokers and business owners

Industry/Entity Type

Real Estate

Colors
0455a3
85abd2
3276b5

Requirements
Must have
• We are a commercial real estate office so we would like this post card to be catchy.

```html
<!DOCTYPE html>
<html lang="en">
<head>
<meta charset="utf-8">
<title>Harborline Realty Postcard</title>
<link rel="stylesheet" href="https://fonts.googleapis.com/css2?family=Oswald:wght@400;500&family=Open+Sans:wght@400;600&display=swap">
<style>
  :root {
    --blue-deep: #0455a3;
    --blue-mid: #3276b5;
    --blue-light: #85abd2;
    --blue-dark: #033f7a;
    --ink: #1c2430;
    --strip: #20262f;
    --paper: #ffffff;
    --stage: #e7e9ec;
    --rule: #9aa3ad;
    --muted: #5d6874;
  }
  * { box-sizing: border-box; margin: 0; padding: 0; }
  html, body { width: 1200px; height: 795px; overflow: hidden; }
  body {
    background: var(--stage);
    font-family: "Open Sans", sans-serif;
    position: relative;
  }
  .postcard {
    position: absolute;
    top: 207px;
    width: 560px;
    height: 380px;
    background: var(--paper);
    overflow: hidden;
    box-shadow: 0 6px 18px rgba(0,0,0,.18);
  }
  .postcard--front { left: 30px; }
  .postcard--back  { left: 610px; background: linear-gradient(120deg, #ffffff 0%, #f4f5f7 55%, #e3e6ea 100%); }

  /* front */
  .hero {
    position: absolute; inset: 0 0 190px 0;
    background: linear-gradient(180deg, #dfe2e6 0%, #c7ccd2 45%, #9ea5ad 100%);
  }
  .brand {
    position: absolute; left: 16px; top: 14px;
    display: flex; align-items: center; gap: 6px;
    background: var(--paper); padding: 5px 9px;
  }
  .brand__mark { width: 10px; height: 10px; background: var(--blue-deep); }
  .brand__name {
    font-family: "Oswald", sans-serif; font-weight: 500;
    font-size: 12px; color: var(--blue-deep); letter-spacing: .5px;
  }
  .headline {
    position: absolute; right: 18px; top: 16px; width: 330px; text-align: right;
    font-family: "Oswald", sans-serif; font-weight: 500;
    font-size: 25px; line-height: 1.1; color: var(--blue-deep); text-transform: uppercase;
  }
  .intro {
    position: absolute; right: 18px; top: 76px; width: 300px; text-align: right;
    font-size: 9.5px; line-height: 1.45; color: var(--ink);
  }
  .buildings {
    position: absolute; left: 0; right: 0; top: 150px; height: 190px;
    display: flex;
  }
  .building {
    flex: 1; position: relative; color: var(--paper);
  }
  .building:nth-child(1) { background: var(--blue-deep); }
  .building:nth-child(2) { background: var(--blue-light); }
  .building:nth-child(3) { background: var(--blue-mid); }
  .building:nth-child(4) { background: var(--blue-dark); }
  .building__photo {
    position: absolute; left: 10px; right: 10px; height: 78px;
  }
  .building:nth-child(1) .building__photo { top: 10px;  background: linear-gradient(135deg, #4f8a3a, #d6b94a 60%, #c15b7a); }
  .building:nth-child(2) .building__photo { top: 34px;  background: linear-gradient(160deg, #7fb2e0, #6e9a4c 60%, #4c7a34); }
  .building:nth-child(3) .building__photo { top: 58px;  background: linear-gradient(160deg, #9cc4ea, #b48a62 55%, #7d5a3c); }
  .building:nth-child(4) .building__photo { top: 82px;  background: linear-gradient(180deg, #d9e6f2, #a7bccf 50%, #6f8a5a); }
  .building__address {
    position: absolute; left: 12px; right: 10px; bottom: 10px;
    font-family: "Oswald", sans-serif; font-size: 12px; line-height: 1.25;
  }
  .building__town { display: block; font-family: "Open Sans", sans-serif; font-size: 9px; opacity: .9; }
  .contact-strip {
    position: absolute; left: 0; right: 0; bottom: 0; height: 40px;
    background: var(--strip); color: var(--paper);
    display: flex; align-items: center; justify-content: center;
    font-size: 9.5px; letter-spacing: .6px; text-transform: uppercase;
  }

  /* back */
  .return-block {
    position: absolute; left: 22px; top: 20px; display: flex; gap: 10px; align-items: flex-start;
  }
  .return-block .brand { position: static; padding: 0; background: none; }
  .return-address { font-size: 8.5px; line-height: 1.4; color: var(--muted); }
  .form-title {
    position: absolute; left: 22px; top: 92px;
    font-family: "Oswald", sans-serif; font-weight: 500; font-size: 20px;
    color: var(--blue-deep); text-transform: uppercase;
  }
  .form-fields {
    position: absolute; left: 22px; top: 138px; width: 260px; list-style: none;
  }
  .form-fields li {
    display: flex; align-items: flex-end; gap: 8px; height: 38px;
    font-size: 9.5px; font-weight: 600; color: var(--ink); text-transform: uppercase; letter-spacing: .5px;
  }
  .form-fields li::after {
    content: ""; flex: 1; border-bottom: 1px solid var(--rule); margin-bottom: 3px;
  }
</style>
</head>
<body>

<section class="postcard postcard--front">
  <div class="hero" role="img" aria-label="Photo of the office building at 586 East Tamsworth Ln set back under a cloudy sky"></div>
  <div class="brand"><span class="brand__mark"></span><span class="brand__name">Harborline Realty</span></div>
  <h1 class="headline">Looking for space for your business</h1>
  <p class="intro">Fill out this postcard with your information or that of a referral looking for office, medical, warehouse or retail space &amp; send it back to receive a $25 gift card to Velvet Lanes, NY.</p>

  <div class="buildings">
    <div class="building">
      <div class="building__photo" role="img" aria-label="Photo of 48 Quillfern Ave with flowers in front"></div>
      <p class="building__address">48 Quillfern Ave<span class="building__town">N. White Plains</span></p>
    </div>
    <div class="building">
      <div class="building__photo" role="img" aria-label="Photo of 212 W Tamsworth Ln with a grass roundabout in front"></div>
      <p class="building__address">212 W Tamsworth Ln.<span class="building__town">Mount Kisco</span></p>
    </div>
    <div class="building">
      <div class="building__photo" role="img" aria-label="Close-up photo of the square building at 417/419 W Tamsworth Ln"></div>
      <p class="building__address">417/419 W Tamsworth Ln<span class="building__town">Mount Kisco</span></p>
    </div>
    <div class="building">
      <div class="building__photo" role="img" aria-label="Photo of 586 East Tamsworth Ln set far back under clouds"></div>
      <p class="building__address">586 East Tamsworth Ln<span class="building__town">Mount Kisco</span></p>
    </div>
  </div>

  <p class="contact-strip">For all space availabilities visit www.harborlinerealty.example or call Owen Trezelle 914 608 3157</p>
</section>

<section class="postcard postcard--back">
  <div class="return-block">
    <div class="brand"><span class="brand__mark"></span><span class="brand__name">Harborline Realty</span></div>
    <p class="return-address">Harborline Realty<br>Attn: Owen Trezelle<br>Mount Kisco, NY</p>
  </div>
  <h2 class="form-title">Enter your details</h2>
  <ul class="form-fields">
    <li>Name</li>
    <li>E-mail</li>
    <li>Referral name</li>
    <li>Phone number</li>
  </ul>
</section>

</body>
</html>
```